Cyber Security Site Design (Products & Consulting)

I need my website redesigned to be engaging, clean, efficient and modern. My company (when its up and running) is going to be concentrated on two things: a few specific products for cyber security as well as cyber security consulting services. The background I bring to the field is having worked with small companies all the way to the largest government organizations and advising them on their security posture and how to improve it. We need the ability to add products and services easily.

For a sample product, you can use either Tarnel (http://www.tarnel-relay.org/) or Vornidex Graywell (https://www.vornidex.com/products/relay-kx-and-enhanced-safe-portal).

It will replace https://dalmorenvue.com/

Target Market(s)

Cyber Security professionals in all verticals

Coding

Coded - Design and coding required

Number of Pages Required

4 page

Font styles to use
Sans Serif

Colors
6b449b

Requirements
Must have
• Ability to easily modify
• Have main page
• Have product specific pages
• Have consulting services pages
• Have executive team information
• Clean, modern design
• Usage of the logo and its color scheme
Nice to have
• I like the idea of a left collapsed sidebar (so icons only) that can expand for text.
• I am also open to a very unique landing page, possibly a shape in the middle (hexagons maybe?) with each of the options there.
Should not have
• Nothing that looks like it came out of a hacker movie

```html
<!DOCTYPE html>
<html lang="en">
<head>
<meta charset="utf-8">
<title>Dalmoren Vue — Cyber Security Products &amp; Consulting</title>
<link href="https://fonts.googleapis.com/css2?family=Montserrat:wght@400;600;700&family=Open+Sans:ital,wght@0,400;0,600;0,700;1,400&display=swap" rel="stylesheet">
<style>
:root{
  --purple:#8e1fbf;
  --purple-dark:#5e137f;
  --magenta:#c81be0;
  --ink:#2b2b33;
  --muted:#6b6b75;
  --line:#d9d9de;
  --footer:#3a3f4a;
  --yellow:#f5d33b;
  --white:#ffffff;
}
*{box-sizing:border-box;margin:0;padding:0}
html,body{width:1200px;height:3152px;overflow:hidden}
body{position:relative;background:var(--white);font-family:"Open Sans",Arial,sans-serif;color:var(--ink)}
.abs{position:absolute}
.heading{font-family:"Montserrat",Arial,sans-serif}
.btn{position:absolute;display:flex;align-items:center;justify-content:center;font-family:"Montserrat",Arial,sans-serif;font-size:10px;font-weight:700;letter-spacing:1px;color:var(--white);background:linear-gradient(var(--magenta),var(--purple-dark));border-radius:3px;box-shadow:0 2px 4px rgba(0,0,0,.35)}
.btn-outline{background:none;border:1px solid rgba(255,255,255,.8);box-shadow:none}
.brand{position:absolute;display:flex;align-items:center;gap:14px}
.brand-dot{width:56px;height:56px;border-radius:50%;background:var(--purple)}
.brand-name{font-family:"Montserrat",Arial,sans-serif;font-weight:700;font-size:30px;color:var(--white);letter-spacing:1px}

/* hero */
.hero{left:0;top:0;width:1200px;height:479px;background:radial-gradient(ellipse at 55% 70%,#5a3b6e 0%,#2f2b4a 45%,#151a2c 100%)}
.menu{left:888px;top:28px;color:var(--white);font-size:12px;display:flex;align-items:center;gap:8px}
.menu i{display:block;width:16px;height:2px;background:#fff;box-shadow:0 -5px 0 #fff,0 5px 0 #fff}
.hero-title{left:0;width:1200px;top:138px;text-align:center;font-size:38px;line-height:50px;font-weight:700;color:var(--white)}
.hero-title span{color:var(--magenta)}
.hero-sub{left:0;width:1200px;top:201px;text-align:center;font-size:15px;line-height:22px;color:#eee}

/* services */
.service-icon{position:absolute;width:114px;height:114px;border-radius:50%;background:#fff;box-shadow:0 3px 10px rgba(0,0,0,.18);display:flex;align-items:center;justify-content:center}
.service-title{position:absolute;width:240px;text-align:center;font-size:12px;letter-spacing:1px;top:648px}
.service-list{position:absolute;top:667px;list-style:none;font-size:11px;color:var(--muted);line-height:19px}
.service-list li{position:relative;padding-left:27px}
.service-list li::before{content:"";position:absolute;left:0;top:6px;width:6px;height:6px;border:1px solid #aaa}

/* newsletter */
.newsletter{left:0;top:778px;width:1200px;height:150px;background:linear-gradient(90deg,#4a4b55,#7a7b84 50%,#3c3d46)}
.news-input{left:343px;top:839px;width:334px;height:29px;background:#fff;border-radius:3px;font-size:9px;color:#999;padding:9px 12px}

/* tools */
.section-title{left:0;width:1200px;text-align:center;font-size:22px;line-height:28px;font-weight:600}
.section-title span{color:var(--magenta)}
.section-sub{left:0;width:1200px;text-align:center;font-size:10px;line-height:17px;color:var(--muted)}
.support-title{left:86px;top:1102px;color:var(--magenta);font-size:22px;line-height:28px;font-weight:700}
.support-head{position:absolute;left:86px;font-family:"Montserrat",Arial,sans-serif;font-size:13px;line-height:18px;font-weight:600;color:#333}
.support-text{position:absolute;left:86px;width:300px;font-family:"Montserrat",Arial,sans-serif;font-size:11px;line-height:19px;font-weight:700}
.market-btn{left:86px;top:1555px;width:145px;height:32px;background:#eee;border-radius:3px;font-size:12px;font-weight:600;display:flex;align-items:center;justify-content:center}
.help-title{left:744px;top:1080px;font-size:24px;line-height:30px;font-weight:600}
.help-item{position:absolute;width:96px;font-size:9px;line-height:11px;font-weight:600}
.help-item b{display:block;font-size:12px;line-height:15px;font-weight:600}
.show-more{left:538px;top:1641px;width:122px;height:28px;border:1px solid #bbb;font-size:10px;display:flex;align-items:center;justify-content:center}

/* testimonial */
.testimonial{left:0;top:1706px;width:1200px;height:301px;background:linear-gradient(120deg,#2a2d3a,#4b4e5c 50%,#23252f)}
.avatar{left:565px;top:1708px;width:68px;height:68px;border-radius:50%;background:linear-gradient(#c9b6a8,#7a6a60);border:3px solid #fff}
.quote{left:0;width:1200px;top:1862px;text-align:center;font-style:italic;font-size:16px;line-height:23px;color:#fff}
.quote-name{left:0;width:1200px;top:1929px;text-align:center;font-size:11px;line-height:14px;font-weight:600;color:#fff}

/* blog */
.timeline{left:603px;top:2127px;width:1px;height:395px;background:var(--line)}
.blog-img{position:absolute;width:197px;height:110px}
.blog-text{position:absolute;width:197px}
.blog-text small{font-size:8px;line-height:12px;color:#999;display:block}
.blog-text h4{font-size:11px;line-height:15px;font-weight:600;margin:3px 0 4px}
.blog-text p{font-size:8px;line-height:12px;color:#999}
.shares{position:absolute;display:flex;gap:5px}
.shares i{width:14px;height:14px;border-radius:50%;display:block}
.more-btn{left:580px;top:2551px;width:34px;height:34px;border-radius:50%;background:var(--purple);color:#fff;font-size:8px;font-weight:700;display:flex;align-items:center;justify-content:center}

/* contact */
.contact{left:0;top:2606px;width:1200px;height:483px;background:radial-gradient(ellipse at 50% 30%,#4a4f63,#2a2e3d 70%)}
.field{position:absolute;background:#fff;border-radius:3px;font-size:10px;color:#999;padding:8px 10px}
.social{left:683px;top:2978px;display:flex;gap:10px}
.social i{display:block;width:26px;height:26px;border-radius:50%}
.footer{left:0;top:3089px;width:1200px;height:63px;background:var(--footer);color:#ddd;font-size:9px;display:flex;align-items:center;padding-left:258px}
</style>
</head>
<body>

<!-- hero -->
<section class="abs hero" role="img" aria-label="Hand reaching toward a glowing circuit board"></section>
<div class="brand" style="left:36px;top:36px"><span class="brand-dot"></span><span class="brand-name">DALMOREN VUE</span></div>
<div class="abs menu">Menu <i></i></div>
<h1 class="abs hero-title heading">CYBER SECURITY <span>CONSULTING</span></h1>
<p class="abs hero-sub">Security products and expert consulting for every kind of team,<br>from small companies to the largest government organizations</p>
<div class="btn" style="left:467px;top:282px;width:126px;height:29px">HIRE US</div>
<div class="btn btn-outline" style="left:610px;top:282px;width:126px;height:29px">OUR PRODUCTS</div>
<svg class="abs" style="left:587px;top:425px" width="24" height="24" viewBox="0 0 24 24"><circle cx="12" cy="12" r="11" fill="none" stroke="#fff" stroke-width="1.5"/><path d="M7 10l5 5 5-5" fill="none" stroke="#fff" stroke-width="1.5"/></svg>

<!-- services -->
<div class="service-icon" style="left:214px;top:517px"><svg width="42" height="42" viewBox="0 0 40 40"><rect x="9" y="17" width="22" height="18" rx="2" fill="none" stroke="#9b3fe0" stroke-width="2"/><path d="M14 17v-5a6 6 0 0112 0v5" fill="none" stroke="#e04fb0" stroke-width="2"/></svg></div>
<div class="service-title" style="left:151px">PRODUCTS</div>
<ul class="service-list" style="left:200px"><li>Tarnel Relay Cache</li><li>Vornidex Graywell Portal</li><li>Access Control Security</li><li>Threat Monitoring</li><li>Lifetime Warranty</li></ul>

<div class="service-icon" style="left:552px;top:517px"><svg width="42" height="42" viewBox="0 0 40 40"><circle cx="20" cy="20" r="8" fill="none" stroke="#9b3fe0" stroke-width="2"/><path d="M20 4v6M20 30v6M4 20h6M30 20h6M9 9l4 4M27 27l4 4M31 9l-4 4M9 31l4-4" stroke="#e04fb0" stroke-width="2"/></svg></div>
<div class="service-title" style="left:489px">CONSULTING</div>
<ul class="service-list" style="left:540px"><li>Security Posture Review</li><li>Risk Assessments</li><li>Compliance Planning</li><li>Incident Response</li><li>Government Advisory</li></ul>

<div class="service-icon" style="left:887px;top:517px"><svg width="42" height="42" viewBox="0 0 40 40"><circle cx="20" cy="20" r="15" fill="none" stroke="#9b3fe0" stroke-width="2"/><path d="M20 10l8 3v7c0 5-4 8-8 10-4-2-8-5-8-10v-7z" fill="none" stroke="#e04fb0" stroke-width="2"/></svg></div>
<div class="service-title" style="left:824px">EXECUTIVE TEAM</div>
<ul class="service-list" style="left:853px"><li>Founder &amp; Principal Consultant</li><li>Chief Technology Officer</li><li>Head of Products</li><li>Client Success Lead</li><li>Security Advisory Board</li></ul>

<!-- newsletter -->
<section class="abs newsletter" role="img" aria-label="Security cameras mounted on a wall"></section>
<div class="abs news-input">Enter your email address for security updates</div>
<div class="btn" style="left:696px;top:839px;width:159px;height:29px">SUBSCRIBE</div>

<!-- tools -->
<h2 class="abs section-title heading" style="top:972px">OUR <span>TOOLS</span></h2>
<p class="abs section-sub" style="top:1001px">Products and services that grow with your security needs,<br>easy to extend as new offerings are added</p>

<h2 class="abs support-title heading">SUPPORT</h2>
<h4 class="support-head" style="top:1174px">FAQ</h4>
<p class="support-text" style="top:1199px">Answers to common questions on licences, setup and support plans.</p>
<h4 class="support-head" style="top:1260px">Product Pages</h4>
<p class="support-text" style="top:1292px">Tarnel relay caching and the Vornidex Graywell secure portal</p>
<h4 class="support-head" style="top:1332px">Consulting Services</h4>
<p class="support-text" style="top:1363px">Posture reviews and improvement plans for small firms up to government bodies</p>
<h4 class="support-head" style="top:1441px">Executive Team</h4>
<p class="support-text" style="top:1473px">Meet the leaders who advise on your security posture and how to improve it</p>
<div class="abs market-btn">Go to Products</div>
<svg class="abs" style="left:263px;top:1520px" width="92" height="92" viewBox="0 0 90 90"><circle cx="45" cy="45" r="42" fill="none" stroke="#111" stroke-width="3"/><path d="M37 20h16v22h12L45 62 25 42h12z" fill="#111"/><rect x="27" y="67" width="36" height="4" fill="#111"/></svg>

<h3 class="abs help-title heading">Online Help</h3>
<svg class="abs" style="left:0;top:1100px" width="1200" height="540" viewBox="0 0 1200 540">
  <path d="M630 31 A245 245 0 0 1 630 521" fill="none" stroke="var(--yellow)" stroke-width="5"/>
  <circle cx="630" cy="31" r="6" fill="var(--yellow)"/><circle cx="630" cy="521" r="6" fill="var(--yellow)"/>
  <g stroke-width="2.5" fill="#ddd">
    <circle cx="752" cy="64" r="10" stroke="#e04848"/><circle cx="843" cy="155" r="10" stroke="#b23fd6"/><circle cx="872" cy="277" r="10" stroke="#3d6fe0"/><circle cx="843" cy="396" r="10" stroke="#2bb8a0"/><circle cx="752" cy="487" r="10" stroke="#7ed321"/>
  </g>
  <g stroke-width="2">
    <line x1="768" y1="64" x2="835" y2="64" stroke="#e04848"/><line x1="859" y1="155" x2="905" y2="155" stroke="#b23fd6"/><line x1="888" y1="277" x2="945" y2="277" stroke="#3d6fe0"/><line x1="859" y1="396" x2="905" y2="396" stroke="#2bb8a0"/><line x1="768" y1="487" x2="820" y2="487" stroke="#7ed321"/>
  </g>
  <g fill="none" stroke="#222" stroke-width="3">
    <circle cx="872" cy="62" r="24"/><rect x="862" y="60" width="20" height="15" rx="2"/><path d="M866 60v-5a6 6 0 0112 0v5"/>
    <rect x="948" y="133" width="46" height="30" rx="3"/><path d="M940 168h62"/>
    <circle cx="985" cy="277" r="20"/><path d="M985 260v34M968 277h34"/>
    <rect x="945" y="373" width="44" height="46" rx="4"/><path d="M967 384l10 4v8c0 6-5 9-10 11-5-2-10-5-10-11v-8z"/>
    <rect x="858" y="456" width="30" height="48" rx="4"/><path d="M868 496h10"/>
  </g>
</svg>
<div class="abs" role="img" aria-label="Fingerprint and password security illustration" style="left:407px;top:1191px;width:384px;height:384px;border-radius:50%;background:radial-gradient(circle at 40% 40%,#6fb8ff,#1d4fb8 60%,#0d1f5c);box-shadow:0 4px 12px rgba(0,0,0,.25)"></div>
<div class="help-item" style="left:914px;top:1142px"><b>Tarnel</b>Relay cache setup and tuning</div>
<div class="help-item" style="left:1006px;top:1224px"><b>Graywell</b>Secure portal guides and updates</div>
<div class="help-item" style="left:1051px;top:1348px"><b>Consulting</b>Book a posture review session</div>
<div class="help-item" style="left:1000px;top:1467px"><b>Compliance</b>Checklists for audits and policies</div>
<div class="help-item" style="left:916px;top:1558px"><b>Team</b>Contact our executive team</div>
<div class="abs show-more">SHOW MORE</div>

<!-- testimonial -->
<section class="abs testimonial" role="img" aria-label="Hand touching a screen of flowing digits"></section>
<div class="abs avatar" role="img" aria-label="Client portrait"></div>
<p class="abs quote">These guys are incredible! They reviewed our security posture in 10 days!<br>Very good service! Highly recommended!</p>
<p class="abs quote-name">Alan Pierce</p>

<!-- blog -->
<h2 class="abs section-title heading" style="top:2029px">OUR <span>BLOG</span></h2>
<p class="abs section-sub" style="top:2062px">Notes from the field on products, consulting work<br>and practical ways to improve your security posture</p>
<div class="abs timeline"></div>

<div class="blog-img" role="img" aria-label="Padlock on a digital circuit" style="left:385px;top:2129px;background:linear-gradient(135deg,#9b6fd8,#5a2fa0)"></div>
<div class="shares" style="left:525px;top:2246px"><i style="background:#3b5998"></i><i style="background:#1da1f2"></i><i style="background:#dd4b39"></i></div>
<div class="blog-text" style="left:614px;top:2124px"><small>15 March 2018</small><h4>Hardening a relay cache with Tarnel</h4><p>Simple steps to lock down caching, logging and access rules before your relay goes live.</p></div>

<div class="blog-text" style="left:385px;top:2264px;text-align:right"><small>22 April 2018</small><h4>Five steps to a stronger posture</h4><p>What we look for first when advising teams, from small firms to large public agencies.</p></div>
<div class="blog-img" role="img" aria-label="Person at a laptop in blue light" style="left:614px;top:2264px;background:linear-gradient(135deg,#3a7fe0,#0b1f4a)"></div>
<div class="shares" style="left:752px;top:2387px"><i style="background:#3b5998"></i><i style="background:#1da1f2"></i><i style="background:#dd4b39"></i></div>
<div class="blog-text" style="left:614px;top:2397px"><small>08 May 2018</small><h4>Securing mobile access with Graywell</h4><p>How the Vornidex Graywell portal keeps remote staff safe on phones and home networks.</p></div>

<div class="blog-img" role="img" aria-label="Smartphone held in a hand" style="left:385px;top:2403px;background:linear-gradient(135deg,#b8b8b0,#5f6260)"></div>
<div class="shares" style="left:525px;top:2521px"><i style="background:#3b5998"></i><i style="background:#1da1f2"></i><i style="background:#dd4b39"></i></div>
<div class="abs more-btn">MORE</div>

<!-- contact -->
<section class="abs contact" role="img" aria-label="Glowing processor on a circuit board"></section>
<h2 class="abs section-title heading" style="top:2661px;color:#fff">SAY <span>HELLO</span></h2>
<p class="abs section-sub" style="top:2697px;color:#ddd">Tell us about your product or consulting needs and our<br>team will get back to you within one business day</p>
<div class="brand" style="left:36px;top:2792px"><span class="brand-dot"></span><span class="brand-name">DALMOREN VUE</span></div>
<div class="field" style="left:351px;top:2789px;width:240px;height:29px">Your Email</div>
<div class="field" style="left:609px;top:2789px;width:240px;height:29px">Subject</div>
<div class="field" style="left:351px;top:2837px;width:498px;height:118px">Your Message</div>
<div class="btn" style="left:351px;top:2976px;width:126px;height:29px">HIRE US</div>
<div class="abs social"><i style="background:#3b5998"></i><i style="background:#1da1f2"></i><i style="background:#dd4b39"></i><i style="background:#d6307f"></i><i style="background:#1769ff"></i></div>

<footer class="abs footer">© 2018 COPYRIGHT Dalmoren Vue</footer>
</body>
</html>
```